Modern Label for cleaning products for the brand Voralux

We need a label design for our line of cleaning products. The label should feature our logo and an image to identify the product's intended use. I've added our logo and an image for use. This only concerns the design of the label on the front of the bottle.

Label dimensions:
Label 1 (500ml bottle with spray): width 58mm x height 115mm
Label 2: (1L bottle): width 73mm x height 140mm
The design must be consistent for both bottles which you find in the pictures.

The bottles to be labeled are white. See the attachment for a photo of the bottles.

The photo must also appear on the label to identify the product's intended use.

Product information:
Brand: Voralux
Product: Sanitary Cleaner

This text must be placed on the label:
"Cleans, descales & freshens. followed with this text: "Ideal for quick and powerful cleaning. A ready-to-use product for everyday use."

- Mention the seperate USP's: Sanitary, Bathroom, Toilet, Wet areas

Appearance: This is a consumer product, but it must have a professional appearance. We would like to see a design that use the color blue from our logo.

Target Market(s)

Consumers who take care of their homes and want to maintain it the correct (professional) way

Font styles to use
Sans Serif

Colors
0054AA
0677BA
7BADD7
CADEEF
E8F1F8

Requirements
Must have
• USP's + use of image and logo + blend in 1 design
Nice to have
• Keep the color of the logo in the design
Should not have
• Comic sans

```html
<!DOCTYPE html>
<html lang="en">
<head>
<meta charset="utf-8">
<title>Voralux Sanitary Cleaner – Front Label</title>
<link rel="stylesheet" href="https://fonts.googleapis.com/css2?family=Poppins:wght@500;600;700&display=swap">
<style>
  :root {
    --blue-deep: #0054AA;
    --blue-mid: #0677BA;
    --blue-bright: #1a8fd8;
    --blue-soft: #7BADD7;
    --blue-pale: #CADEEF;
    --blue-mist: #E8F1F8;
    --ink: #0b0f17;
    --white: #ffffff;
    --page: #ffffff;
  }
  html, body {
    margin: 0;
    padding: 0;
    width: 842px;
    height: 1200px;
    overflow: hidden;
    background: var(--page);
  }
  .canvas {
    width: 842px;
    height: 1200px;
    display: flex;
    align-items: center;
    justify-content: center;
  }
  .label {
    width: 420px;
    height: 729px;
    display: block;
    font-family: "Poppins", sans-serif;
  }
  .claim { fill: var(--blue-bright); font-weight: 700; font-size: 7.6px; letter-spacing: 0.2px; }
  .brand-name { fill: var(--ink); font-weight: 700; font-size: 25px; letter-spacing: -0.4px; }
  .usage { fill: var(--white); font-weight: 600; font-size: 8.6px; }
  .benefit-small { fill: var(--white); font-weight: 600; font-size: 5px; }
  .benefit-big { fill: var(--white); font-weight: 700; font-size: 8.8px; }
  .usp { fill: var(--white); font-weight: 600; font-size: 6.6px; letter-spacing: 0.3px; }
</style>
</head>
<body>
<main class="canvas">
  <svg class="label" viewBox="0 0 190 330" xmlns="http://www.w3.org/2000/svg" aria-label="Voralux Sanitary Cleaner front label">
    <defs>
      <clipPath id="label-shape">
        <rect x="0" y="0" width="190" height="270" rx="10"/>
      </clipPath>
      <linearGradient id="ground" x1="0" y1="0" x2="1" y2="0.2">
        <stop offset="0" stop-color="var(--ink)"/>
        <stop offset="0.6" stop-color="#0d2440"/>
        <stop offset="1" stop-color="var(--blue-mid)"/>
      </linearGradient>
      <linearGradient id="top-swoosh" x1="0" y1="0" x2="1" y2="0">
        <stop offset="0" stop-color="var(--blue-deep)"/>
        <stop offset="0.5" stop-color="var(--blue-bright)"/>
        <stop offset="1" stop-color="var(--ink)"/>
      </linearGradient>
      <linearGradient id="swoosh" x1="0" y1="0" x2="1" y2="1">
        <stop offset="0" stop-color="var(--blue-bright)"/>
        <stop offset="0.6" stop-color="var(--blue-mid)"/>
        <stop offset="1" stop-color="var(--ink)"/>
      </linearGradient>
      <linearGradient id="oval" x1="0" y1="0" x2="1" y2="1">
        <stop offset="0" stop-color="var(--white)"/>
        <stop offset="0.5" stop-color="var(--blue-mist)"/>
        <stop offset="1" stop-color="var(--white)"/>
      </linearGradient>
      <linearGradient id="scene" x1="0" y1="0" x2="1" y2="1">
        <stop offset="0" stop-color="var(--blue-mid)"/>
        <stop offset="0.45" stop-color="#3aa6e6"/>
        <stop offset="1" stop-color="var(--blue-bright)"/>
      </linearGradient>
      <linearGradient id="tab" x1="0" y1="0" x2="0" y2="1">
        <stop offset="0" stop-color="var(--blue-mid)"/>
        <stop offset="1" stop-color="var(--blue-bright)"/>
      </linearGradient>
    </defs>

    <!-- lower tab with product uses -->
    <ellipse class="label-tab" cx="95" cy="268" rx="72" ry="54" fill="url(#tab)"/>
    <text class="usp" text-anchor="middle">
      <tspan x="95" y="290">Sanitary · Bathroom</tspan>
      <tspan x="95" y="301">Toilet · Wet areas</tspan>
    </text>

    <g clip-path="url(#label-shape)">
      <rect x="0" y="0" width="190" height="270" fill="url(#ground)"/>

      <!-- product-use photo area -->
      <rect class="use-photo" x="0" y="130" width="190" height="140" fill="url(#scene)"
            role="img" aria-label="Photo of a clean bathroom with sink and tiles in blue tones"/>
      <rect x="0" y="235" width="120" height="35" fill="var(--ink)" opacity="0.25"/>

      <!-- top sweep -->
      <ellipse cx="150" cy="70" rx="150" ry="40" transform="rotate(-18 150 70)" fill="url(#top-swoosh)" opacity="0.9"/>

      <!-- swooshes -->
      <ellipse cx="100" cy="128" rx="112" ry="80" transform="rotate(-22 100 128)" fill="url(#swoosh)"/>
      <ellipse cx="102" cy="132" rx="100" ry="68" transform="rotate(-22 102 132)" fill="var(--blue-pale)" opacity="0.6"/>
      <ellipse cx="100" cy="128" rx="96" ry="64" transform="rotate(-22 100 128)" fill="url(#oval)"/>

      <!-- brand -->
      <circle class="brand-dot" cx="78" cy="106" r="19" fill="none" stroke="var(--blue-deep)" stroke-width="6"/>
      <text class="brand-name" x="116" y="166" text-anchor="middle" transform="rotate(-22 116 166)">Voralux</text>

      <!-- claim -->
      <text class="claim" transform="rotate(-33 8 20)">
        <tspan x="6" y="20">CLEANS,</tspan>
        <tspan x="6" y="29">DESCALES</tspan>
        <tspan x="6" y="38">&amp; FRESHENS.</tspan>
      </text>

      <!-- usage copy -->
      <text class="usage">
        <tspan x="11" y="238">A ready-to-use</tspan>
        <tspan x="11" y="249">product for</tspan>
        <tspan x="11" y="260">everyday use.</tspan>
      </text>
      <text text-anchor="end">
        <tspan class="benefit-small" x="181" y="234">Ideal for</tspan>
        <tspan class="benefit-big" x="181" y="244">quick and</tspan>
        <tspan class="benefit-big" x="181" y="254">powerful</tspan>
        <tspan class="benefit-small" x="181" y="261">cleaning</tspan>
      </text>
    </g>
  </svg>
</main>
</body>
</html>
```